VELNA BROCADE

Project name: “Velna Brocade” website
Objective: To create an elegant website,
intuitive and responsive to present this
what is “Velna Brocade”
See attached specifications.

```html
<!DOCTYPE html>
<html lang="en">
<head>
<meta charset="utf-8">
<title>Velna Brocade</title>
<link rel="stylesheet" href="https://fonts.googleapis.com/css2?family=Jost:wght@500;600&family=Poppins:wght@400;500;600;700&display=swap">
<style>
:root{
  --green:#3a5a3d;
  --green-line:#4e8a3a;
  --mint:#dce5dd;
  --white:#ffffff;
  --ink:#222;
  --hero-top:#3b3f5c;
  --hero-bottom:#4a5a3a;
}
*{box-sizing:border-box;margin:0;padding:0}
html,body{width:1200px;height:2310px;overflow:hidden;background:var(--white)}
body{position:relative;font-family:"Poppins",sans-serif;color:var(--ink)}
.abs{position:absolute}
.heading{font-family:"Jost",sans-serif;font-weight:600;text-transform:uppercase}
/* header */
.brand-box{left:140px;top:0;width:186px;height:143px;background:var(--green);display:flex;align-items:center;justify-content:center}
.brand-box span{font-family:"Jost",sans-serif;font-weight:600;color:var(--white);font-size:17px;letter-spacing:1.5px}
.phone-line{right:119px;top:27px;font-weight:500;font-size:19px;color:var(--green);display:flex;align-items:center;gap:10px}
.main-nav{left:487px;top:83px;display:flex;gap:37px;font-weight:500;font-size:17px;color:var(--green)}
/* hero */
.hero{left:0;top:141px;width:1200px;height:650px}
.hero-photo{position:absolute;inset:0;background:linear-gradient(180deg,var(--hero-top) 0%,#4b4a5e 45%,#5d4a34 75%,var(--hero-bottom) 100%)}
.hero-title{left:0;top:176px;width:1200px;text-align:center;color:var(--white);font-size:52px;line-height:60px}
.hero-btn{left:481px;top:315px;width:238px;height:57px;border:2px solid var(--white);border-radius:30px;background:var(--green);color:var(--white);font-weight:700;font-size:18px;display:flex;align-items:center;justify-content:center;letter-spacing:-0.3px}
/* intro */
.frame-line{left:362px;top:826px;width:155px;height:293px;border:1.5px solid var(--green-line)}
.intro-photo{left:172px;top:843px;width:320px;height:480px;background:linear-gradient(160deg,#1f4a2f 0%,#4f7a33 45%,#7a8e3a 80%,#8a8a3a 100%)}
.seal{left:99px;top:1122px;width:146px;height:146px;border-radius:50%;background:var(--white);box-shadow:0 8px 24px rgba(0,0,0,.12)}
.intro-title{left:584px;top:852px;font-size:37px;line-height:44px;color:var(--green)}
.intro-lead{left:584px;top:955px;width:480px;font-size:17px;line-height:22px;color:#333}
.rule{left:584px;top:1023px;width:455px;height:1px;background:#cfcfcf}
.intro-sub{left:587px;top:1042px;font-weight:600;font-size:22px;color:var(--green)}
.intro-copy{left:588px;top:1090px;width:490px}
.intro-body{font-size:14.5px;line-height:23.2px;color:#444;letter-spacing:-0.1px}
.read-btn{margin-top:20px;width:163px;height:52px;border-radius:26px;background:var(--green);color:var(--white);font-weight:700;font-size:15.5px;display:flex;align-items:center;justify-content:center}
/* about */
.about{left:0;top:1436px;width:1200px;height:487px;background:var(--green)}
.about-title{left:133px;top:140px;color:var(--white);font-size:38px}
.about-body{left:133px;top:204px;width:500px;color:var(--white);font-size:15px;line-height:23.2px;letter-spacing:-0.1px}
.about-mark{left:733px;top:60px;width:340px;height:350px}
/* footer */
.footer{left:0;top:1923px;width:1200px;height:387px;background:var(--mint)}
.divider{top:82px;width:1.5px;height:310px;background:var(--green)}
.foot-name{left:100px;top:220px;width:295px;text-align:center;font-family:"Jost",sans-serif;font-weight:600;font-size:25px;letter-spacing:3px;color:var(--green)}
.foot-badge{left:196px;top:102px;width:104px;height:104px;border:3px solid var(--green);border-radius:50%}
.copyright{left:133px;top:273px;font-size:15px;color:#333}
.foot-head{top:90px;font-family:"Jost",sans-serif;font-weight:500;font-size:32px;color:var(--green)}
.contact-item{left:509px;display:flex;align-items:center;gap:14px;font-size:15.5px;line-height:22px;color:#222}
.icon-dot{width:44px;height:44px;border-radius:50%;background:var(--green);border:3px solid var(--white);display:flex;align-items:center;justify-content:center;flex:none}
.foot-links{left:951px;top:157px;list-style:none;font-size:15.5px;line-height:32px;color:#222}
</style>
</head>
<body>

<header>
  <div class="abs brand-box"><span>VELNA BROCADE</span></div>
  <div class="abs phone-line">
    <svg width="16" height="16" viewBox="0 0 24 24"><path fill="#3a5a3d" d="M6.6 10.8a15 15 0 0 0 6.6 6.6l2.2-2.2c.3-.3.7-.4 1-.2 1.1.4 2.3.6 3.6.6.6 0 1 .4 1 1V20c0 .6-.4 1-1 1A17 17 0 0 1 3 4c0-.6.4-1 1-1h3.5c.6 0 1 .4 1 1 0 1.3.2 2.5.6 3.6.1.3 0 .7-.2 1z"/></svg>
    Call: (555)410-2287
  </div>
  <nav class="abs main-nav"><span>Home</span><span>What We Do</span><span>About Us</span><span>Location</span><span>Contact</span><span>FAQ</span></nav>
</header>

<section class="abs hero">
  <div class="hero-photo" role="img" aria-label="Craftsman-style house at dusk surrounded by tall pine trees"></div>
  <svg class="abs" style="left:0;top:0" width="1200" height="650" viewBox="0 0 1200 650">
    <path d="M0 456 C120 520 260 530 400 538 C700 550 1000 560 1200 640 L1200 650 L0 650 Z" fill="#fff"/>
    <path d="M0 630 C80 575 120 540 300 530 C320 530 360 535 400 538 C260 530 120 520 0 456 Z" fill="#3a5a3d"/>
    <path d="M0 456 C120 520 260 530 400 538 C700 550 1000 560 1200 640" fill="none" stroke="#4e8a3a" stroke-width="2"/>
  </svg>
  <h1 class="abs heading hero-title">Welcome to<br>Velna Brocade</h1>
  <div class="abs hero-btn">GET STARTED HERE</div>
</section>

<section>
  <div class="abs frame-line"></div>
  <div class="abs intro-photo" role="img" aria-label="Hand placing a small model house on green grass"></div>
  <div class="abs seal"></div>
  <h2 class="abs heading intro-title">Velna Brocade<br>What we are doing</h2>
  <p class="abs intro-lead">Lorem ipsum dolor sit amet, consectetur adipiscing elit, sed do eiusmod tempor incididunt ut labore<br>.</p>
  <div class="abs rule"></div>
  <h3 class="abs intro-sub">Lorem ipsum dolor sit amet, consectetur</h3>
  <div class="abs intro-copy">
    <p class="intro-body">Lorem ipsum dolor sit amet, consectetur adipiscing elit, sed do eiusmod tempor incididunt ut labore et dolore magna aliqua Quis ipsum suspendisse ultrices gravida. Risus commodo viv rra maecenas accumsan lacus vel facilisis. Lorem ipsum dolor sit amet, consectetur adipiscing elit, sed do eiusmod tempor incididunt ut labore et dolore magna aliqua.</p>
    <div class="read-btn">READ MORE</div>
  </div>
</section>

<section class="abs about">
  <h2 class="abs heading about-title">About Velna Brocade</h2>
  <p class="abs about-body">Lorem ipsum dolor sit amet, consectetur adipiscing elit, sed do eiusmod tempor incididunt ut labore et dolore magna aliqua Quis ipsum suspendisse ultrices gravida. Risus commodo viv rra maecenas accumsan lacus vel facilisis. Lorem ipsum dolor sit amet, consectetur adipiscing elit, sed do eiusmod tempor incididunt ut labore et dolore magna aliqua.</p>
  <svg class="abs about-mark" viewBox="0 0 340 350"><circle cx="170" cy="175" r="165" fill="none" stroke="#dce5dd" stroke-width="7"/></svg>
</section>

<footer class="abs footer">
  <div class="abs divider" style="left:454px"></div>
  <div class="abs divider" style="left:886px"></div>
  <div class="abs foot-badge"></div>
  <div class="abs foot-name">VELNA BROCADE</div>
  <p class="abs copyright">© 2025 All Rights are Reserved.</p>

  <h4 class="abs foot-head" style="left:507px">Contact</h4>
  <div class="abs contact-item" style="top:165px">
    <span class="icon-dot"><svg width="16" height="20" viewBox="0 0 16 20"><path fill="#fff" d="M8 0a8 8 0 0 0-8 8c0 6 8 12 8 12s8-6 8-12a8 8 0 0 0-8-8zm0 11a3 3 0 1 1 0-6 3 3 0 0 1 0 6z"/></svg></span>
    <span>42 Alder Lane<br>Greyford, ST 00000</span>
  </div>
  <div class="abs contact-item" style="top:231px">
    <span class="icon-dot"><svg width="18" height="18" viewBox="0 0 24 24"><path fill="#fff" d="M6.6 10.8a15 15 0 0 0 6.6 6.6l2.2-2.2c.3-.3.7-.4 1-.2 1.1.4 2.3.6 3.6.6.6 0 1 .4 1 1V20c0 .6-.4 1-1 1A17 17 0 0 1 3 4c0-.6.4-1 1-1h3.5c.6 0 1 .4 1 1 0 1.3.2 2.5.6 3.6.1.3 0 .7-.2 1z"/></svg></span>
    <span>Phone: 555-410-2287<br>Fax: 555-410-2288</span>
  </div>
  <div class="abs contact-item" style="top:296px;gap:10px">
    <span class="icon-dot"><svg width="18" height="14" viewBox="0 0 18 14"><rect width="18" height="14" rx="2" fill="#fff"/><path d="M1 2l8 6 8-6" fill="none" stroke="#3a5a3d" stroke-width="1.6"/></svg></span>
    <span>Emial:<br>hello@velnabrocade.example</span>
  </div>

  <h4 class="abs foot-head" style="left:951px">Links</h4>
  <ul class="abs foot-links"><li>Home</li><li>About</li><li>What We Do</li><li>Contact</li><li>FAQ</li></ul>
</footer>

</body>
</html>
```